Small Box Design - For launch into retail market

We need artwork for small boxes that we are going to be using for the retail market. I will upload the type of box we are going to be using. The example we are uploading is of a different company that sells the same products. We would like our Logo on the box as as our web address (www.kestonbarlow.example). The rest is up to you. Please contact with any questions.

Target Market(s)

Distributors, Retailers of Fasteners

Industry/Entity Type

Manufacture

Colors
0355a3
3176b5
fbee3f
fbf289

Requirements
Must have
• Our logo, our web address www.kestonbarlow.example
• Somewhere on the box Washers . Stampings . Assemblies . Bearings (most likely below our logo somewhere)
Nice to have
• Blue is our corporate colour, but it's not essential. You can suggest any colours and we will consider.

```html
<!DOCTYPE html>
<html lang="en">
<head>
<meta charset="utf-8">
<title>Keston Barlow – Small Retail Box Artwork</title>
<link rel="stylesheet" href="https://fonts.googleapis.com/css2?family=Saira:ital,wght@0,300;0,500;1,800&display=swap">
<style>
  :root {
    --blue-deep: #0355a3;
    --blue-mid: #1f5fae;
    --blue-light: #3176b5;
    --yellow: #fbee3f;
    --yellow-soft: #fbf289;
    --white: #ffffff;
    --backdrop: #e9e7e7;
    --mark-tan: #c9a97a;
  }
  * { margin: 0; padding: 0; box-sizing: border-box; }
  html, body {
    width: 1200px; height: 960px; overflow: hidden;
    background: var(--backdrop);
    font-family: "Saira", sans-serif;
  }
  .artwork {
    position: absolute; left: 60px; top: 250px;
    width: 1080px; height: 460px;
    display: flex;
    box-shadow: 0 10px 30px rgba(0,0,0,0.12);
  }
  .panel { position: relative; height: 460px; overflow: hidden; background: var(--white); }
  .panel--side { width: 320px; border-right: 1px solid #d8dbe2; }
  .panel--front { width: 760px; }
  .panel__graphics { position: absolute; inset: 0; }

  .brand {
    position: absolute; display: flex; align-items: center;
    color: var(--blue-light); font-weight: 500; white-space: nowrap;
  }
  .brand__dot { border-radius: 50%; background: var(--mark-tan); flex: none; }
  .brand--front { left: 40px; top: 195px; font-size: 46px; gap: 16px; }
  .brand--front .brand__dot { width: 42px; height: 42px; }
  .brand--side { left: 16px; top: 110px; font-size: 17px; gap: 7px; }
  .brand--side .brand__dot { width: 16px; height: 16px; }

  .product-list {
    position: absolute; list-style: none;
    color: var(--white); font-style: italic; font-weight: 800;
    letter-spacing: 0.5px; transform-origin: left top;
  }
  .product-list--front { left: 568px; top: 150px; font-size: 17px; line-height: 36px; transform: rotate(-3deg); }
  .product-list--side { left: 200px; top: 160px; font-size: 12px; line-height: 30px; transform: rotate(12deg); }

  .web-address {
    position: absolute; color: var(--blue-deep); font-weight: 300; white-space: nowrap;
    letter-spacing: 0.3px; transform-origin: left top;
  }
  .web-address--front { left: 520px; top: 335px; font-size: 15px; transform: rotate(-6deg); }
  .web-address--side { left: 112px; top: 334px; font-size: 11px; transform: rotate(11deg); }
</style>
</head>
<body>
  <main class="artwork" aria-label="Small retail box artwork, flat">
    <section class="panel panel--side">
      <svg class="panel__graphics" width="320" height="460" viewBox="0 0 320 460" aria-hidden="true">
        <polygon points="200,0 320,0 320,460 100,460" fill="var(--blue-mid)"/>
        <polygon points="200,0 218,0 118,460 100,460" fill="var(--blue-light)"/>
        <polygon points="92,320 320,365 320,402 80,355" fill="var(--yellow)"/>
      </svg>
      <div class="brand brand--side"><span class="brand__dot"></span>Keston Barlow</div>
      <ul class="product-list product-list--side">
        <li>WASHERS</li><li>STAMPINGS</li><li>ASSEMBLIES</li><li>BEARINGS</li>
      </ul>
      <p class="web-address web-address--side">www.kestonbarlow.example</p>
    </section>

    <section class="panel panel--front">
      <svg class="panel__graphics" width="760" height="460" viewBox="0 0 760 460" aria-hidden="true">
        <polygon points="545,0 760,0 760,460 320,460" fill="var(--blue-mid)"/>
        <polygon points="545,0 572,0 347,460 320,460" fill="var(--blue-light)"/>
        <polygon points="232,358 760,300 760,352 218,412" fill="var(--yellow-soft)"/>
        <polygon points="232,358 520,326 505,380 218,412" fill="var(--yellow)" opacity="0.6"/>
      </svg>
      <div class="brand brand--front"><span class="brand__dot"></span>Keston Barlow</div>
      <ul class="product-list product-list--front">
        <li>WASHERS</li><li>STAMPINGS</li><li>ASSEMBLIES</li><li>BEARINGS</li>
      </ul>
      <p class="web-address web-address--front">www.kestonbarlow.example</p>
    </section>
  </main>
</body>
</html>
```